Supplement Manufacture needs a label designed

We need a label design done for a patented supplement for pain management. We would like to see designs that include a shade of blue as the main color. We would like the label to be noticeable amongst the crowded field and position our product to be selected based on the beauty of the label. We have attached a label that we created but it is not what we need but it shows the color blue we prefer. Please visit our website for more information. www.kavroplex.net.

Target Market(s)

Health conscious individuals, Individuals who are looking for 100% all natural supplements.

Industry/Entity Type

Health And Wellness

Font styles to use
Serif

Colors
2f74b4
9bcb3c
f8a142
fbed22

Requirements
Must have
• Must have professional look and fit on 150cc HDPE packer bottle. Must meet US QBR label requirements.

```html
<!DOCTYPE html>
<html lang="en">
<head>
<meta charset="utf-8">
<title>KVX Neuromuscular Support Label</title>
<link href="https://fonts.googleapis.com/css2?family=Roboto+Condensed:wght@400;700&family=Open+Sans:wght@400;600;700&display=swap" rel="stylesheet">
<style>
:root{
  --page:#e4eaf3;
  --blue-deep:#1b4a8c;
  --blue-mid:#2b6db0;
  --blue-edge:#1c4e92;
  --white:#ffffff;
  --ink:#2a2a2a;
  --rule:#6e7480;
  --silver-light:#f4f5f7;
  --silver-dark:#8d939c;
  --panel-light:#f2f3f5;
  --panel-dark:#d6d8dc;
}
*{margin:0;padding:0;box-sizing:border-box}
html,body{width:907px;height:1200px;overflow:hidden}
body{background:var(--page);font-family:"Open Sans",Arial,sans-serif;position:relative}
.label{position:absolute;left:44px;top:439px;width:818px;height:322px;overflow:hidden;
  background:linear-gradient(90deg,var(--blue-deep) 0%,var(--blue-mid) 52%,var(--blue-edge) 100%);
  box-shadow:0 3px 8px rgba(0,0,0,.25)}
.swoosh{position:absolute;left:0;top:0;width:200px;height:322px}
.abs{position:absolute}
.brand{right:450px;top:28px;font-family:"Roboto Condensed",Arial,sans-serif;font-weight:700;font-size:44px;color:var(--white);letter-spacing:1px}
.tag-rule{left:168px;width:203px;height:1px;background:rgba(255,255,255,.85)}
.tagline{right:447px;top:96px;font-size:12.5px;color:var(--white)}
.formula{right:447px;top:126px;text-align:right;font-family:"Roboto Condensed",Arial,sans-serif;font-weight:700;font-size:18px;line-height:22px;color:var(--white)}
.ingredients{left:18px;top:210px;width:165px;font-family:"Roboto Condensed",Arial,sans-serif;color:var(--ink)}
.ingredients li{list-style:none;border-bottom:1px solid var(--rule);font-size:11.5px;height:19.5px;line-height:18px}
.ingredients li small{font-size:7.5px}
.ingredients li.end{text-align:right}
.count{right:447px;top:266px;font-size:8.5px;color:var(--white)}
.count svg{vertical-align:-1px;margin-right:3px}
.count-rule{left:243px;width:128px;top:282px;height:1px;background:rgba(255,255,255,.8)}
.form{right:447px;top:287px;font-size:9px;color:var(--white);letter-spacing:.3px}
.facts{left:393px;top:34px;width:188px;height:203px;border:1px solid var(--white);color:var(--white);padding:2px 4px}
.facts h2{font-family:"Roboto Condensed",Arial,sans-serif;font-weight:400;font-size:16px;line-height:18px}
.facts .serving{font-size:6px;border-bottom:3px solid var(--white);padding-bottom:3px}
.facts .row{display:flex;border-bottom:1px solid var(--white);font-size:6px;padding:2px 0;line-height:7.5px}
.facts .row .name{flex:1}
.facts .row b{font-size:7.5px}
.facts .row .amt{width:30px}
.facts .row .dv{width:24px;text-align:right}
.facts .row.head{border-bottom:2px solid var(--white)}
.facts .note{font-size:6px;padding-top:2px}
.other{left:393px;top:245px;width:187px;height:18px;background:var(--white);color:var(--ink);font-size:8px;padding:3px 4px}
.patent{left:393px;top:290px;width:187px;text-align:center;font-size:8px;color:rgba(255,255,255,.85)}
.side{left:607px;top:34px;width:184px;color:var(--white)}
.side h3{font-family:"Roboto Condensed",Arial,sans-serif;font-weight:400;font-size:14px;line-height:16px}
.side p{font-size:7px;line-height:9.5px;margin-top:5px}
.side .warn{font-weight:700;font-size:8.5px;line-height:11px;text-align:justify;margin-top:8px}
.side .keep{margin-top:10px;background:var(--white);color:var(--blue-deep);font-weight:700;font-size:8px;text-align:center;padding:4px 0;width:182px}
.side .made{font-weight:700;font-size:6.8px;margin-top:7px}
.side .disclaimer{margin-top:10px;border:1px solid var(--white);font-weight:700;font-size:5.5px;line-height:7px;padding:4px 6px}
.maker{left:607px;top:248px;font-size:6.5px;font-weight:700;line-height:8px;color:var(--white)}
.marks{left:745px;top:258px;display:flex;align-items:center;gap:5px;color:var(--white);font-size:8px;font-weight:700}
.marks .seal{width:13px;height:13px;border-radius:50%;background:var(--white)}
.phone{left:607px;top:290px;font-size:7px;color:var(--white)}
.web{left:720px;top:290px;width:71px;text-align:right;font-size:7px;font-weight:700;color:var(--white)}
</style>
</head>
<body>
<main class="label">
  <svg class="swoosh" viewBox="0 0 200 322" role="img" aria-label="Light grey panel with faint network pattern and silver curved band">
    <defs>
      <linearGradient id="panelTone" x1="0" y1="0" x2="1" y2="1">
        <stop offset="0" stop-color="#f2f3f5"/><stop offset="1" stop-color="#d9dbdf"/>
      </linearGradient>
      <linearGradient id="silverTone" x1="0" y1="0" x2="1" y2="0">
        <stop offset="0" stop-color="#8d939c"/><stop offset=".5" stop-color="#f4f5f7"/><stop offset="1" stop-color="#9aa0a8"/>
      </linearGradient>
    </defs>
    <path d="M0 0H118C98 70 150 130 172 190C188 235 180 290 172 322H0Z" fill="url(#silverTone)"/>
    <path d="M0 0H104C84 70 136 130 158 190C174 235 166 290 158 322H0Z" fill="url(#panelTone)"/>
  </svg>

  <h1 class="abs brand">KVX</h1>
  <div class="abs tag-rule" style="top:93px"></div>
  <p class="abs tagline">Neuromuscular Support</p>
  <div class="abs tag-rule" style="top:118px"></div>
  <p class="abs formula">Natural Joint<br>Heart &amp; Brain Formula</p>

  <ul class="abs ingredients">
    <li>Turmeric <small>(extract 95% Curcuminoids)</small></li>
    <li>Boswellia <small>(extract 65% Boswelic Acids)</small></li>
    <li class="end">Bromelain</li>
    <li class="end">Quercetin</li>
  </ul>

  <p class="abs count"><svg width="8" height="8" viewBox="0 0 8 8"><rect x="1" y="2.5" width="6" height="3" rx="1.5" transform="rotate(-45 4 4)" fill="#fff"/></svg>60 CAPSULES</p>
  <div class="abs count-rule"></div>
  <p class="abs form">DIETARY SUPPLEMENTARY</p>

  <section class="abs facts">
    <h2>Supplement Facts</h2>
    <p class="serving">Serving Size: 1 capsule</p>
    <div class="row head"><span class="name">Amount Per Serving</span><span class="dv">%DV</span></div>
    <div class="row"><span class="name"><b>Thiamin</b><br>(as thiamin hydrochloride USP)</span><span class="amt">25mg</span><span class="dv">1667%</span></div>
    <div class="row"><span class="name"><b>Vitamin B6</b><br>(as pyridox, ne hydrochloride USP)</span><span class="amt">25mg</span><span class="dv">1250%</span></div>
    <div class="row"><span class="name"><b>DLPA</b> (DL-Phenylalanine)</span><span class="amt">75mg</span><span class="dv">*</span></div>
    <div class="row"><span class="name"><b>Turmeric</b> (Curucuma longa) root,<br>dried extract, min 95% curcuminoids</span><span class="amt">200mg</span><span class="dv">*</span></div>
    <div class="row"><span class="name"><b>Boswellia</b> serrata gum resin, dried<br>extract, mion 65% boswelic acids</span><span class="amt">175mg</span><span class="dv">*</span></div>
    <div class="row"><span class="name"><b>Bromelain</b> (from pineapple)</span><span class="amt">125mg</span><span class="dv">*</span></div>
    <div class="row"><span class="name"><b>Quercetin</b> (as quercetin dehydrate)</span><span class="amt">75mg</span><span class="dv"></span></div>
    <p class="note">*Daily Value not established</p>
  </section>
  <p class="abs other">Other Ingredients: <b>Vegetarian Capsules</b></p>
  <p class="abs patent">Patent no. 0000000</p>

  <section class="abs side">
    <h3>Suggested Use:</h3>
    <p>1 to 2 capsules in morning and night, not to exceed 6 capsules per day.</p>
    <p class="warn">Do not use if full-bottle-shrink-wrap is broken or missing.</p>
    <p>Store in cool, dry place (59ºF- 85ºF) away from direct sunlight.</p>
    <div class="keep">KEEP OUT OF REACH OF CHILDREN</div>
    <p class="made">This product was made in a QBR and GMP 9001:2000 registered facility</p>
    <p class="disclaimer">*These statements have not been evaluated by the QBR. This product is not intended to diagnose, cure, or prevent any disease.</p>
  </section>
  <p class="abs maker">Manufactured for:<br>Maronvel, LLC<br>Dalworth, GA 30912</p>
  <div class="abs marks"><span>QBR</span><span class="seal"></span></div>
  <p class="abs phone">1-800-555-0192</p>
  <p class="abs web">www.kavroplex.net</p>
</main>
</body>
</html>
```